Quillory Points website re-design and

the institute of massage therapy is ready for a new website. The current website is around 12 years old and it looks old. Luckily the clients is not against changing the colors so the new design does not have to use the current ugly green color scheme. Be creative! Make it pretty, modern and inviting. The current colors look like mold. Nobody likes mold. I have attached the logo asset file as well as a txt document that details the new website design parameters

1 page

```html
<!DOCTYPE html>
<html lang="en">
<head>
<meta charset="utf-8">
<title>Halvern Institute of Bodywork</title>
<link href="https://fonts.googleapis.com/css2?family=Montserrat:wght@400;500;600;700&family=Cinzel:wght@600;700&display=swap" rel="stylesheet">
<style>
:root{
  --blue:#5aafe4;
  --orange:#f7b532;
  --ink:#1a1a1a;
  --text:#333;
  --muted:#555;
  --grey-bg:#f2f4f6;
  --dark:#111;
  --white:#fff;
}
*{box-sizing:border-box;margin:0;padding:0}
html,body{width:1200px;height:5268px;overflow:hidden}
body{position:relative;font-family:'Montserrat',sans-serif;color:var(--text);background:var(--white)}
.abs{position:absolute}
.center{text-align:center}

/* header */
.site-header{left:0;top:0;width:1200px;height:76px;background:var(--white)}
.brand{left:160px;top:18px;display:flex;align-items:center;gap:10px}
.brand-dot{width:34px;height:34px;border-radius:50%;background:var(--ink)}
.brand-name{font-size:17px;font-weight:600;color:var(--ink);letter-spacing:.5px;line-height:1.1}
.login-btn{left:861px;top:20px;width:86px;height:33px;background:var(--orange);color:#fff;font-size:12px;font-weight:600;display:flex;align-items:center;justify-content:center;gap:5px}
.cart{left:971px;top:26px;display:flex;align-items:center;gap:6px;font-size:12px;font-weight:600;color:var(--ink)}
.main-nav{left:0;top:76px;width:1200px;height:38px;background:var(--blue);display:flex;justify-content:space-between;padding:0 160px 0 163px;align-items:center}
.main-nav span{font-size:12px;font-weight:500;color:#fff;letter-spacing:.3px}
.main-nav .active{color:var(--orange)}

/* hero */
.hero{left:0;top:114px;width:1200px;height:571px;background:linear-gradient(135deg,#b9a48e 0%,#8c7563 30%,#5b4a42 55%,#a48877 75%,#6f5a4f 100%)}
.hero-shade{left:0;top:114px;width:1200px;height:571px;background:rgba(0,0,0,.28)}
.hero-title{left:0;top:300px;width:1200px;font-family:'Cinzel',serif;font-weight:700;font-size:33px;color:#fff;line-height:42px;letter-spacing:1px}
.search{left:296px;top:425px;display:flex;gap:10px}
.search .field{height:49px;background:#fff;font-size:10px;color:#888;display:flex;align-items:center;padding:0 14px}
.search .kw{width:219px}
.search .hours{width:217px;justify-content:space-between}
.search .go{width:149px;height:49px;background:var(--orange);color:#fff;font-size:14px;font-weight:600;display:flex;align-items:center;justify-content:center}

/* section titles */
.sec-title{left:0;width:1200px;font-size:31px;font-weight:600;color:var(--ink)}
.about-text{left:180px;top:818px;width:840px;font-size:11.5px;line-height:24px;color:var(--text)}
.btn{background:var(--orange);color:#fff;font-size:13px;font-weight:600;display:flex;align-items:center;justify-content:center}

/* provides */
.provides{left:0;top:1110px;width:1200px;height:644px;background:var(--grey-bg)}
.tab{top:1261px;width:226px;height:45px;font-size:14px;font-weight:600;display:flex;align-items:center;justify-content:center;color:#fff;background:#000}
.tab.on{background:var(--blue)}
.card{top:1345px;width:280px;height:331px;background:#fff}
.card .img{height:161px}
.card h3{margin-top:22px;font-size:15px;font-weight:600;color:var(--ink);text-align:center}
.card p{margin:8px auto 0;width:230px;font-size:11px;line-height:24px;text-align:center;color:var(--text)}
.card a{display:block;margin-top:4px;text-align:center;font-size:11px;color:var(--orange);text-decoration:underline;font-weight:500}

/* free course */
.free{left:161px;top:1866px;width:877px;height:376px;background:var(--blue)}
.free-person{left:188px;top:1831px;width:302px;height:444px;border-radius:140px 140px 30px 30px;background:linear-gradient(180deg,#8a6a55 0%,#f0e6dc 35%,#9aa0a8 70%,#e8e8e8 100%)}
.free h2{position:absolute;left:424px;top:92px;font-size:32px;font-weight:600;color:#fff;letter-spacing:.5px}
.free p{position:absolute;left:424px;top:140px;font-size:19px;line-height:36px;color:#fff}
.free .btn{position:absolute;left:422px;top:231px;width:147px;height:43px;font-size:12.5px}

/* reasons */
.reasons-title{left:0;top:2352px;width:1200px;font-size:32px;font-weight:500;line-height:42px;color:var(--ink)}
.reasons-sub{left:0;top:2445px;width:1200px;font-size:18px;font-weight:500;color:var(--orange)}
.reason{top:2508px;width:280px;text-align:center}
.reason .icon{width:90px;height:90px;border-radius:50%;background:#111;margin:0 auto;display:flex;align-items:center;justify-content:center}
.reason h4{margin-top:20px;font-size:17px;font-weight:600;color:var(--ink)}
.reason p{margin:8px auto 0;width:255px;font-size:11px;line-height:24.5px;color:var(--text)}
.extra-title{left:0;top:2756px;width:1200px;font-size:18px;font-weight:600;color:var(--ink)}
.extra-text{left:180px;top:2786px;width:842px;font-size:11px;line-height:24.5px;color:var(--text)}

/* faq */
.faq-bg{left:0;top:2954px;width:1200px;height:838px;background:linear-gradient(120deg,#f7f6f4 0%,#fbfaf9 40%,#eeece9 70%,#f8f7f6 100%)}
.faq-title{left:0;top:3030px;width:1200px;font-size:31px;font-weight:600;color:var(--ink)}
.faq-sub{left:0;top:3081px;width:1200px;font-size:15px;color:var(--text)}
.faq-list{left:239px;top:3134px;width:720px;display:flex;flex-direction:column;gap:10px}
.faq{background:#fff;padding:0 30px 0 14px;min-height:50px;display:flex;align-items:center;justify-content:space-between;font-size:11px;font-weight:600;color:var(--ink);line-height:22px;box-shadow:0 1px 4px rgba(0,0,0,.05)}
.faq.open{display:block;padding:12px 30px 12px 14px;position:relative}
.faq.open p{font-weight:400;font-size:10px;line-height:21px;color:var(--muted);margin-top:14px;border-top:1px solid #eee;padding-top:4px}
.faq.open svg{position:absolute;right:30px;top:18px}

/* contact & courses */
.contact-line{left:0;top:3863px;width:1200px;font-size:17px;font-weight:600;line-height:31px;color:var(--ink)}
.courses{left:161px;top:3990px;width:877px;height:818px;background:#fff;box-shadow:0 0 18px rgba(0,0,0,.08)}
.courses h2{position:absolute;top:70px;width:100%;text-align:center;font-size:31px;font-weight:600;color:var(--ink)}
.course-col{position:absolute;top:137px;list-style:none}
.course-col li{font-size:11.5px;line-height:24.5px;color:var(--text);padding-left:20px;position:relative}
.course-col li::before{content:"›";position:absolute;left:0;top:0;color:var(--ink);font-weight:600}

/* footer */
.footer{left:0;top:4889px;width:1200px;height:338px;background:var(--blue)}
.foot-brand{left:0;top:4982px;width:1200px;display:flex;justify-content:center;align-items:center;gap:12px}
.foot-brand .brand-dot{background:#fff}
.foot-brand .brand-name{color:#fff;font-size:22px}
.foot-nav{left:0;top:5064px;width:1200px;display:flex;justify-content:center;gap:18px;font-size:14px;color:#fff;font-weight:500}
.foot-phone{left:0;top:5116px;width:1200px;display:flex;justify-content:center;align-items:center;gap:10px;font-size:15px;color:#fff}
.copyright{left:0;top:5227px;width:1200px;height:41px;background:var(--dark);color:#fff;font-size:11px;display:flex;align-items:center;justify-content:center}
</style>
</head>
<body>

<header class="abs site-header">
  <div class="abs brand"><span class="brand-dot"></span><span class="brand-name">HALVERN INSTITUTE<br>OF BODYWORK</span></div>
  <div class="abs login-btn">
    <svg width="10" height="11" viewBox="0 0 10 11"><circle cx="5" cy="3" r="2.3" fill="none" stroke="#fff" stroke-width="1.2"/><path d="M1 10.5c0-2.5 1.8-4 4-4s4 1.5 4 4" fill="none" stroke="#fff" stroke-width="1.2"/></svg>LOGIN
  </div>
  <div class="abs cart">CART
    <svg width="22" height="20" viewBox="0 0 22 20"><path d="M2 6h14l-1.5 11h-11z" fill="none" stroke="#111" stroke-width="1.4"/><path d="M6 6V4a3 3 0 0 1 6 0v2" fill="none" stroke="#111" stroke-width="1.4"/><circle cx="17" cy="4" r="4" fill="#5aafe4"/></svg>
  </div>
</header>
<nav class="abs main-nav">
  <span class="active">HOME</span><span>COURSES</span><span>GUIDELINES</span><span>FAQs</span><span>POLICIES</span><span>CONTACT</span><span>ABOUT</span>
</nav>

<div class="abs hero" role="img" aria-label="Photograph of an instructor teaching massage students around a client on a massage table"></div>
<div class="abs hero-shade"></div>
<h1 class="abs hero-title center">Committed to Excellence in<br>Massage Therapy Continuing Education</h1>
<div class="abs search">
  <div class="field kw">Search by keyword</div>
  <div class="field hours">Number of CE Hours <svg width="9" height="6" viewBox="0 0 9 6"><path d="M1 1l3.5 3.5L8 1" fill="none" stroke="#666" stroke-width="1.2"/></svg></div>
  <div class="go">SEARCH</div>
</div>

<h2 class="abs sec-title center" style="top:758px">The Halvern Institute of Bodywork</h2>
<p class="abs about-text center">The Halvern Institute of Bodywork is committed to providing the best online home study continuing education courses available to massage therapists. Halvern Institute of Bodywork is approved by the National Board for Touch Therapy Standards (NBTTS) as a continuing education Approved Provider.<br>Provider # 104410-00. Our massage CEUs/credits are also valid for ATG and BPA. We are approved by the State Board of Massage (Provider #MCE118) and CredTrack (Provider #50-2207). Our massage therapy continuing education courses are valid for most state massage therapy CEU requirements.</p>
<div class="abs btn" style="left:525px;top:989px;width:150px;height:45px">READ MORE</div>

<section class="abs provides"></section>
<h2 class="abs sec-title center" style="top:1184px">Halvern Institute of Bodywork Provides</h2>
<div class="abs tab on" style="left:255px">POPULAR PACKAGES</div>
<div class="abs tab" style="left:497px">CERTIFICATIONS</div>
<div class="abs tab" style="left:740px">OUR COURSES</div>

<div class="abs card" style="left:161px">
  <div class="img" role="img" aria-label="Photograph of hands resting on a pregnant belly" style="background:linear-gradient(135deg,#c58f6f,#e8c3a8 55%,#a8705a)"></div>
  <h3>PREGNANCY / DOULA</h3>
  <p>Courses and packages to become certified in every stage of childbearing, from infertility to infant massage</p>
  <a>FIND OUT MORE</a>
</div>
<div class="abs card" style="left:460px">
  <div class="img" role="img" aria-label="Photograph of a city skyline with a plain round badge" style="background:linear-gradient(180deg,#c9d6e2,#7d8ea0 55%,#3d4a58)"></div>
  <h3>FLORIDA LAWS &amp; PACKAGES</h3>
  <p>Courses and packages required to obtain, reinstate, or renew your Florida massage therapy license</p>
  <a>FIND OUT MORE</a>
</div>
<div class="abs card" style="left:758px">
  <div class="img" role="img" aria-label="Photograph of hands massaging a foot" style="background:linear-gradient(135deg,#f1ede9,#d9b9a3 55%,#f5f1ed)"></div>
  <h3>REFLEXOLOGY</h3>
  <p>Please note that this course looks at medical research that has been performed to support the use</p>
  <a>FIND OUT MORE</a>
</div>

<section class="abs free">
  <h2>TAKE A FREE COURSE</h2>
  <p>Click Here To Get Started Today &amp;<br>Try Our FREE Online Course!</p>
  <div class="btn">GET STARTED</div>
</section>
<div class="abs free-person" role="img" aria-label="Photograph of a smiling student sitting cross-legged with a laptop, giving a thumbs up"></div>

<h2 class="abs reasons-title center">Three Reasons Why The Halvern Institute of<br>Bodywork Offers</h2>
<p class="abs reasons-sub center">The Best Online Continuing Education Experience</p>

<div class="abs reason" style="left:160px">
  <div class="icon"><svg width="44" height="40" viewBox="0 0 44 40" fill="none" stroke="#fff" stroke-width="2"><rect x="4" y="4" width="36" height="24" rx="2"/><path d="M2 32h40M12 20l6-6 5 5 8-9"/></svg></div>
  <h4>Instant Access and Results</h4>
  <p>Simply enroll in any of our online continuing education courses &amp; you will have instant access to your course. As soon...[+]</p>
</div>
<div class="abs reason" style="left:458px">
  <div class="icon"><svg width="42" height="42" viewBox="0 0 42 42" fill="none" stroke="#fff" stroke-width="2"><circle cx="21" cy="21" r="16"/><path d="M14 21l5 5 9-10"/></svg></div>
  <h4>Hassle-Free</h4>
  <p>With our online courses, you work at your own pace. Fit your CEUs into your independent lifestyle. You can log in...[+]</p>
</div>
<div class="abs reason" style="left:756px">
  <div class="icon"><svg width="44" height="40" viewBox="0 0 44 40" fill="none" stroke="#fff" stroke-width="2"><path d="M22 4l14 5v10c0 9-6 14-14 17C14 33 8 28 8 19V9z"/><path d="M16 20l5 5 8-9"/></svg></div>
  <h4>Risk Free Sample Course</h4>
  <p>Take a free course to see exactly how our system operates. This gives you the peace of mind of knowing what to expect...[+]</p>
</div>

<h3 class="abs extra-title center">And If Those Three Reasons Aren't Enough...</h3>
<p class="abs extra-text center">Another reason to take our home study continuing education courses: We donate 10% of profits to charitable organizations. By doing business with us, you help to support many valuable organizations. We have made donations to Bright Horizon Camps, Veteran Trail Ride, Unity Games, Harbor Relief Agency, and many other worthy charities. Thank you for your continued support while together we help these wonderful organizations perform their valuable work.</p>

<section class="abs faq-bg" role="img" aria-label="Faded photograph of a bright massage room"></section>
<h2 class="abs faq-title center">Frequently Asked Questions</h2>
<p class="abs faq-sub center">About Our Online Continuing Education Courses</p>
<div class="abs faq-list">
  <div class="faq open">I am currently in massage school. Can I start taking your pregnancy massage course now so when I<br>become licensed I'll be ready to work on pregnant women?
    <svg width="12" height="8" viewBox="0 0 12 8"><path d="M1 7l5-5 5 5" fill="none" stroke="#111" stroke-width="1.5"/></svg>
    <p>Yes. Many massage therapy students begin taking continuing education courses as they near the end of their schooling. You can do this not only with our pregnancy massage course, but with any of our other specialized courses as well.</p>
  </div>
  <div class="faq">Do I have to be a licensed massage therapist to take your courses?<svg width="12" height="8" viewBox="0 0 12 8"><path d="M1 1l5 5 5-5" fill="none" stroke="#111" stroke-width="1.5"/></svg></div>
  <div class="faq">Are your online courses downloadable to my computer?<svg width="12" height="8" viewBox="0 0 12 8"><path d="M1 1l5 5 5-5" fill="none" stroke="#111" stroke-width="1.5"/></svg></div>
  <div class="faq">Will your online courses work on my phone, tablet, or other device?<svg width="12" height="8" viewBox="0 0 12 8"><path d="M1 1l5 5 5-5" fill="none" stroke="#111" stroke-width="1.5"/></svg></div>
  <div class="faq">Can I log in and out while taking an online course, or do I have to take it all at once?<svg width="12" height="8" viewBox="0 0 12 8"><path d="M1 1l5 5 5-5" fill="none" stroke="#111" stroke-width="1.5"/></svg></div>
  <div class="faq">How do I print an additional certificate?<svg width="12" height="8" viewBox="0 0 12 8"><path d="M1 1l5 5 5-5" fill="none" stroke="#111" stroke-width="1.5"/></svg></div>
  <div class="faq">Does the Halvern Institute of Bodywork automatically report course completions to CredTrack?<svg width="12" height="8" viewBox="0 0 12 8"><path d="M1 1l5 5 5-5" fill="none" stroke="#111" stroke-width="1.5"/></svg></div>
  <div class="faq" style="min-height:56px">Does the Halvern Institute of Bodywork report our course completions to the NBTTS, BPA, ATG, or<br>any other agencies or state massage therapy boards?<svg width="12" height="8" viewBox="0 0 12 8"><path d="M1 1l5 5 5-5" fill="none" stroke="#111" stroke-width="1.5"/></svg></div>
</div>

<p class="abs contact-line center">Please Feel Free To Contact Us At The Above Contact Link If You Have Any Questions About<br>How We Can Help You Attain Your Continuing Education Goals. Thank You.</p>

<section class="abs courses">
  <h2>Available Course Titles</h2>
  <ul class="course-col" style="left:78px">
    <li>Certified Fertility Massage Therapist</li><li>Certified Massage Doula</li><li>Customize Your Own Package</li><li>Anatomy Fascial Lines</li><li>Board Certified Renewal, Package 1</li><li>Board Certified Renewal, Package 3</li><li>Deep Tissue Therapy</li><li>Draping Your Client (Ethics Standard V)</li><li>Ethics – Communication</li><li>Ethics – Listening</li><li>Facilitated PNF Stretching</li><li>Florida Laws &amp; Rules – 10 hours #20-471205</li><li>Florida Renewal 6 CE package – Laws, PME, Ethics</li><li>Human Trafficking Awareness and Prevention, 1 CE</li><li>Maryland Package</li><li>Orthopedic Massage for the Extremities</li><li>Pathology – Deep Vein Thrombosis</li><li>Pathology – Morton Foot Structure</li><li>Pathology – Sciatic Pain</li><li>Pathology – Varicose Veins</li><li>Prenatal Massage Techniques (Step Two)</li><li>Reflexology for Feet and Hands</li><li>Research – Pregnancy and Labor Massage</li><li>Seven Mistakes Massage Therapists Make</li><li>Sports &amp; Exercise Massage</li>
  </ul>
  <ul class="course-col" style="left:471px">
    <li>Certified Infant Massage Therapist–Instructor</li><li>Certified Prenatal Massage Therapist</li><li>100 CE Package</li><li>Aromatherapy for Massage</li><li>Board Certified Renewal, Package 2</li><li>Communicable Diseases &amp; HIV</li><li>Diversity and Cultural Awareness</li><li>Ethics – Boundary Setting (Standard V)</li><li>Ethics – Confidentiality</li><li>Ethics – Professionalism</li><li>Fibromyalgia (Stop the Suffering)</li><li>Florida Laws &amp; Rules – 2 hours #20-58832</li><li>Hot Stone Massage</li><li>Human Trafficking Awareness and Prevention, 2 CEs</li><li>New York Package</li><li>Orthopedic Massage for the Spine</li><li>Pathology – Edema</li><li>Pathology – Plantar Fasciitis</li><li>Pathology – Shoulder Dysfunction</li><li>Prenatal Massage Fundamentals (Step One)</li><li>Prevention of Medical Errors for Massage</li><li>Research – Infant Massage</li><li>Research – Reflexology</li><li>Spa Therapy Techniques</li><li>Stretching Anatomy</li>
  </ul>
</section>

<footer class="abs footer"></footer>
<div class="abs foot-brand"><span class="brand-dot"></span><span class="brand-name">HALVERN INSTITUTE OF BODYWORK</span></div>
<div class="abs foot-nav"><span>HOME</span><span>|</span><span>COURSES</span><span>|</span><span>GUIDELINES</span><span>|</span><span>FAQs</span><span>|</span><span>POLICIES</span><span>|</span><span>CONTACT</span><span>|</span><span>ABOUT</span><span>|</span><span>LOGIN</span></div>
<div class="abs foot-phone">
  <svg width="20" height="20" viewBox="0 0 20 20"><path d="M4 2l3 0 1.5 4-2 1.5a11 11 0 0 0 6 6l1.5-2 4 1.5v3c0 1-1 2-2 2C9 18 2 11 2 4c0-1 1-2 2-2z" fill="none" stroke="#fff" stroke-width="1.4"/></svg>
  PHONE : 417-555-0148
</div>
<div class="abs copyright">Copyright © 2022 Halvern Institute of Bodywork. All Rights Reserved.</div>

</body>
</html>
```